Now Leasing Banner

Looking for a banner that says the following information approx 4' x 30'

Now Leasing Maplewood Terrace 925-318-6054

Target Market(s)

Drive by traffic

Industry/Entity Type

Residential property management

Requirements
Must have
• Clear and readable from a distance

```html
<!DOCTYPE html>
<html lang="en">
<head>
<meta charset="utf-8">
<title>Now Leasing Banner – Maplewood Terrace</title>
<link rel="stylesheet" href="https://fonts.googleapis.com/css2?family=Bebas+Neue&family=Roboto:ital,wght@1,900&display=swap">
<style>
  :root {
    --page-bg: #e8e9ed;
    --navy: #00143f;
    --navy-deep: #000a1f;
    --ink: #00030a;
    --red: #ee0a0a;
    --white: #ffffff;
    --gold-light: #fbf1b8;
    --gold: #e3c46a;
    --gold-dark: #9c7a2a;
    --photo-top: #c9a47e;
    --photo-bottom: #5d7048;
  }
  * { margin: 0; padding: 0; box-sizing: border-box; }
  html, body {
    width: 1200px;
    height: 1200px;
    overflow: hidden;
    background: var(--page-bg);
  }
  .banner {
    position: absolute;
    left: 520px;
    top: 0;
    width: 160px;
    height: 1200px;
    overflow: hidden;
  }
  .banner-art {
    position: absolute;
    inset: 0;
    width: 160px;
    height: 1200px;
    display: block;
  }
  .banner-text {
    position: absolute;
    left: 0;
    width: 100%;
    text-align: center;
    color: var(--white);
    font-family: "Bebas Neue", "Oswald", sans-serif;
    line-height: 1;
    transform: translateY(-50%);
  }
  .headline-now { top: 549px; font-size: 36px; }
  .headline-leasing { top: 589px; font-size: 36px; }
  .property-name {
    position: absolute;
    left: 80px;
    top: 751px;
    font-family: "Bebas Neue", "Oswald", sans-serif;
    font-size: 66px;
    line-height: 1;
    color: var(--white);
    white-space: nowrap;
    transform: translate(-50%, -50%) rotate(90deg);
  }
  .property-suffix { top: 908px; font-size: 36px; }
  .phone {
    position: absolute;
    left: 0;
    width: 100%;
    text-align: center;
    font-family: "Roboto", "Arial", sans-serif;
    font-weight: 900;
    font-style: italic;
    line-height: 1;
    transform: translateY(-50%);
    background: linear-gradient(180deg, var(--gold-light) 0%, var(--gold) 50%, var(--gold-dark) 100%);
    -webkit-background-clip: text;
    background-clip: text;
    color: transparent;
  }
  .phone-area { top: 965px; font-size: 58px; }
  .phone-prefix { top: 1020px; font-size: 58px; }
  .phone-line { top: 1075px; font-size: 58px; }
</style>
</head>
<body>
  <div class="banner">
    <svg class="banner-art" viewBox="837 0 258 1932" preserveAspectRatio="none" xmlns="http://www.w3.org/2000/svg">
      <defs>
        <linearGradient id="navy-fade" x1="0" y1="0" x2="0" y2="1">
          <stop offset="0" stop-color="var(--navy)"/>
          <stop offset="0.55" stop-color="var(--navy)"/>
          <stop offset="0.8" stop-color="var(--navy-deep)"/>
          <stop offset="1" stop-color="var(--ink)"/>
        </linearGradient>
        <linearGradient id="photo-tone" x1="0" y1="0" x2="0" y2="1">
          <stop offset="0" stop-color="var(--photo-top)"/>
          <stop offset="1" stop-color="var(--photo-bottom)"/>
        </linearGradient>
        <linearGradient id="red-shade" x1="0" y1="0" x2="1" y2="1">
          <stop offset="0" stop-color="var(--red)"/>
          <stop offset="1" stop-color="#c50606"/>
        </linearGradient>
      </defs>

      <rect class="banner-field" x="837" y="0" width="258" height="1932" fill="url(#navy-fade)"/>

      <polygon class="photo-area" role="img" aria-label="Photo of a high-rise residential tower at sunset above a leafy neighbourhood"
               points="837,0 1095,0 1095,487 955,627 837,487" fill="url(#photo-tone)"/>

      <polygon class="red-sash" points="837,745 1095,487 1095,645 837,900" fill="url(#red-shade)"/>

      <polygon class="red-corner" points="837,1810 966,1932 837,1932" fill="var(--red)"/>
      <polygon class="red-corner" points="1095,1810 966,1932 1095,1932" fill="var(--red)"/>
    </svg>

    <div class="banner-text headline-now">NOW</div>
    <div class="banner-text headline-leasing">LEASING</div>
    <div class="property-name">MAPLEWOOD</div>
    <div class="banner-text property-suffix">TERRACE</div>

    <div class="phone phone-area">925</div>
    <div class="phone phone-prefix">318</div>
    <div class="phone phone-line">6054</div>
  </div>
</body>
</html>
```